Agriculture Business Need a Responsive Web Design

We need a Responsive Web Design for a Agriculture Business
We deliver agriculture data insight for farmers, media, salespersons and other that have an interrest in Agriculture.
Our products is a Velorind - a application that helps people with insight on farms, and what this farms have deliveried of products. Products like Milk, grains, eggs, slaughtering of livestock, chicken, sheep and other slaughter of animals. Data about size of farms. We deliver stats about these farms. Compeare farms.

Agriculture businesses

Agriculture

1 page

Sans Serif

• Responsive design. I.e the design shall be used on smartphones to desktop browsers. I think 2 columns on big screens that will collapse to 1 one small screens.

```html
<!DOCTYPE html>
<html lang="en">
<head>
<meta charset="utf-8">
<title>Velorind — Agriculture Data Insight</title>
<link rel="stylesheet" href="https://fonts.googleapis.com/css2?family=PT+Sans:wght@400;700&display=swap">
<style>
  :root {
    --green: #3fae49;
    --ink: #111111;
    --body-text: #222222;
    --white: #ffffff;
    --footer-bg: #151515;
    --bottom-bar: #000000;
    --footer-muted: #d8d8d8;
    --social: #3a4450;
  }
  * { margin: 0; padding: 0; box-sizing: border-box; }
  html, body { width: 1200px; height: 2892px; overflow: hidden; }
  body {
    position: relative;
    font-family: "PT Sans", Arial, sans-serif;
    color: var(--body-text);
    background: var(--white);
  }
  .abs { position: absolute; }

  /* Hero */
  .hero {
    position: absolute; left: 0; top: 0; width: 1200px; height: 674px;
    background: linear-gradient(180deg, #6f8a58 0%, #59773f 35%, #3f5e2a 70%, #2e4a1f 100%);
  }
  .hero-shade { position: absolute; inset: 0; background: rgba(0,0,0,0.12); }
  .brand { left: 35px; top: 50px; font-size: 24px; color: var(--white); letter-spacing: 1px; }
  .main-nav { left: 367px; top: 50px; display: flex; gap: 27px; }
  .main-nav a { color: var(--white); text-decoration: none; font-size: 18px; position: relative; }
  .main-nav a.is-active::before {
    content: ""; position: absolute; left: 0; right: 0; top: -14px; height: 6px; background: var(--green);
  }
  .nav-rule { left: 0; top: 98px; width: 1200px; height: 1px; background: rgba(255,255,255,0.35); }
  .hero-title { left: 0; width: 1200px; top: 200px; text-align: center; color: var(--white); font-size: 84px; font-weight: 400; line-height: 1; }
  .hero-sub { left: 0; width: 1200px; top: 290px; text-align: center; color: var(--white); font-size: 38px; font-weight: 700; line-height: 1.2; }
  .hero-lede { left: 300px; width: 600px; top: 342px; text-align: center; color: var(--white); font-size: 20px; line-height: 26px; }
  .hero-btn {
    height: 46px; border: 1px solid var(--white); color: var(--white); font-size: 16px;
    display: flex; align-items: center; justify-content: center; letter-spacing: 0.5px;
  }

  /* Feature rows */
  .feature-title { font-size: 46px; font-weight: 400; color: var(--ink); line-height: 1.2; }
  .feature-text { font-size: 15px; line-height: 24px; color: var(--body-text); width: 575px; }
  .outline-btn {
    border: 1px solid #333; font-size: 13px; color: var(--ink);
    display: flex; align-items: center; justify-content: center; background: var(--white);
  }

  /* Cards */
  .card-media { width: 347px; height: 226px; }
  .card-title { font-size: 18px; color: var(--green); text-transform: uppercase; width: 360px; }
  .card-text { font-size: 18px; line-height: 24px; color: var(--body-text); width: 347px; }

  /* Footer */
  .site-footer { left: 0; top: 2467px; width: 1200px; height: 376px; background: var(--footer-bg); }
  .footer-brand { left: 35px; top: 2525px; font-size: 32px; color: var(--white); letter-spacing: 1px; }
  .footer-heading { font-size: 24px; color: var(--white); font-weight: 400; }
  .footer-text { left: 414px; top: 2564px; width: 330px; font-size: 14px; line-height: 24px; color: var(--footer-muted); }
  .social-dot { width: 34px; height: 34px; border-radius: 50%; background: var(--social); }
  .bottom-bar {
    left: 0; top: 2843px; width: 1200px; height: 49px; background: var(--bottom-bar);
    color: var(--white); font-size: 18px; display: flex; align-items: center; justify-content: center;
  }
</style>
</head>
<body>

<header class="hero" role="img" aria-label="Photo of a green wheat field">
  <div class="hero-shade"></div>
</header>
<div class="abs brand">VELORIND</div>
<nav class="abs main-nav">
  <a class="is-active" href="#">HOME</a>
  <a href="#">ELEMENTS</a>
  <a href="#">FEATURES</a>
  <a href="#">EXTRAS</a>
  <a href="#">PAGES</a>
  <a href="#">BLOG</a>
  <a href="#">GALLERY</a>
  <a href="#">SHOP</a>
</nav>
<svg class="abs" style="left:1090px;top:46px" width="100" height="34" viewBox="0 0 100 34" aria-hidden="true">
  <circle cx="12" cy="12" r="8" fill="none" stroke="#fff" stroke-width="3"/>
  <line x1="18" y1="18" x2="28" y2="28" stroke="#fff" stroke-width="4" stroke-linecap="round"/>
  <path d="M62 8 h5 l4 16 h17 l3 -11 h-21" fill="none" stroke="#fff" stroke-width="3" stroke-linejoin="round"/>
  <circle cx="74" cy="30" r="2.5" fill="#fff"/>
  <circle cx="86" cy="30" r="2.5" fill="#fff"/>
</svg>
<div class="abs nav-rule"></div>

<h1 class="abs hero-title">Velorind</h1>
<p class="abs hero-sub">farm data insight</p>
<p class="abs hero-lede">Insight on farms and what they deliver: milk, grains, eggs and livestock, with stats on farm size</p>
<div class="abs hero-btn" style="left:385px;top:432px;width:190px">SEE ALL STATISTICS</div>
<div class="abs hero-btn" style="left:659px;top:432px;width:154px">ABOUT US</div>
<svg class="abs" style="left:30px;top:305px" width="1140" height="44" viewBox="0 0 1140 44" aria-hidden="true">
  <polyline points="16,4 4,22 16,40" fill="none" stroke="#fff" stroke-width="5"/>
  <polyline points="1124,4 1136,22 1124,40" fill="none" stroke="#fff" stroke-width="5"/>
</svg>

<!-- Feature: farm production data -->
<section>
  <h2 class="abs feature-title" style="left:35px;top:788px">FARM DATA INSIGHT</h2>
  <p class="abs feature-text" style="left:35px;top:856px">Velorind shows what each farm has delivered: milk, grains, eggs and the slaughter of livestock, chicken and sheep. Clear statistics for farmers, media and salespersons.</p>
  <div class="abs outline-btn" style="left:35px;top:951px;width:127px;height:41px">Read more</div>
  <svg class="abs" style="left:0;top:746px" width="1200" height="492" viewBox="0 0 1200 492" role="img" aria-label="Photo of a combine harvester cutting a golden wheat field">
    <defs>
      <linearGradient id="harvestTone" x1="0" y1="0" x2="0" y2="1">
        <stop offset="0" stop-color="#3e2f3a"/>
        <stop offset="0.45" stop-color="#8a6a3a"/>
        <stop offset="0.7" stop-color="#c78a3a"/>
        <stop offset="1" stop-color="#a8692a"/>
      </linearGradient>
    </defs>
    <polygon points="0,484 1200,0 1200,492 0,492" fill="url(#harvestTone)"/>
  </svg>
</section>

<!-- Feature: compare farms -->
<section>
  <svg class="abs" style="left:0;top:1345px" width="1200" height="483" viewBox="0 0 1200 483" role="img" aria-label="Photo of rows of green crops under a blue sky">
    <defs>
      <linearGradient id="fieldTone" x1="0" y1="0" x2="0" y2="1">
        <stop offset="0" stop-color="#6f8fa6"/>
        <stop offset="0.2" stop-color="#4e7a3a"/>
        <stop offset="0.55" stop-color="#3f8a2f"/>
        <stop offset="1" stop-color="#2f6f22"/>
      </linearGradient>
    </defs>
    <polygon points="0,0 1200,483 0,483" fill="url(#fieldTone)"/>
  </svg>
  <h2 class="abs feature-title" style="left:607px;top:1358px">COMPARE FARMS</h2>
  <p class="abs feature-text" style="left:607px;top:1426px">Put farms side by side. Compare farm size, yearly output and product mix, and see how each farm has developed over time with easy charts and tables.</p>
  <div class="abs outline-btn" style="left:607px;top:1521px;width:128px;height:41px">Read more</div>
</section>

<!-- News cards -->
<section>
  <div class="abs card-media" style="left:35px;top:1929px;background:linear-gradient(160deg,#8fc25a,#4f9a38 60%,#3d7f2c)" role="img" aria-label="Aerial photo of green terraced fields"></div>
  <p class="abs card-title" style="left:35px;top:2170px">Farm size statistics</p>
  <p class="abs card-text" style="left:35px;top:2202px">See how large farms are in every region, from small family farms to big estates.</p>
  <div class="abs outline-btn" style="left:35px;top:2282px;width:101px;height:35px">Read more</div>

  <div class="abs card-media" style="left:425px;top:1929px;background:linear-gradient(45deg,#2f6a1c,#6fae2a 55%,#e8e67a)" role="img" aria-label="Photo of young tea leaves in sunlight"></div>
  <p class="abs card-title" style="left:425px;top:2170px">Milk, grain and egg output</p>
  <p class="abs card-text" style="left:425px;top:2202px">Track what every farm has delivered of milk, grains and eggs year by year.</p>
  <div class="abs outline-btn" style="left:425px;top:2282px;width:101px;height:35px">Read more</div>

  <div class="abs card-media" style="left:818px;top:1929px;background:linear-gradient(180deg,#d9dde6,#e9c98a 55%,#c7893a)" role="img" aria-label="Photo of a yellow combine harvester in a wheat field"></div>
  <p class="abs card-title" style="left:818px;top:2170px">Livestock slaughter data</p>
  <p class="abs card-text" style="left:818px;top:2202px">Figures for cattle, chicken, sheep and other livestock sent to slaughter.</p>
  <div class="abs outline-btn" style="left:818px;top:2282px;width:101px;height:35px">Read more</div>
</section>

<!-- Footer -->
<footer>
  <div class="abs site-footer"></div>
  <div class="abs footer-brand">VELORIND</div>
  <h3 class="abs footer-heading" style="left:414px;top:2516px">Our Services</h3>
  <p class="abs footer-text">Agriculture data insight for farmers, media, salespersons and all others with an interest in farming and farms.</p>
  <h3 class="abs footer-heading" style="left:896px;top:2516px">Connect With Us</h3>
  <div class="abs social-dot" style="left:900px;top:2571px" aria-label="Social profile"></div>
  <div class="abs social-dot" style="left:949px;top:2571px" aria-label="Social profile"></div>
  <div class="abs social-dot" style="left:998px;top:2571px" aria-label="Social profile"></div>
  <div class="abs bottom-bar">Copyright © 2016 Velorind</div>
</footer>

</body>
</html>
```